3D Brochure
Brochure
Project: 3D Brochure
3D Brochure - Environment
Creative Brief
Environment
Corporate, Industrial
Trifold brochure. Must include some "Bleed" for printing.

```html
<!DOCTYPE html>
<html lang="en">
<head>
<meta charset="utf-8">
<title>Tri-Point Environmental Brochure – Content Side</title>
<link rel="stylesheet" href="https://fonts.googleapis.com/css2?family=Arimo:wght@400;700&display=swap">
<style>
  :root {
    --paper: #ffffff;
    --ink: #1f1f1f;
    --navy: #0b2d55;
    --blue: #14508f;
    --blue-mid: #2a6db0;
    --blue-light: #5e9bd3;
    --heading-bar: #0a2546;
    --text-light: #ffffff;
    --crop: #555555;
    --logo-fade: #e9eef3;
  }
  * { box-sizing: border-box; margin: 0; padding: 0; }
  html, body { width: 1200px; height: 922px; overflow: hidden; background: var(--paper); }
  body { position: relative; font-family: "Arimo", Arial, sans-serif; color: var(--ink); }

  .sheet-label {
    position: absolute; left: 14px; top: 14px;
    font-size: 13px; font-weight: 700; letter-spacing: 0.2px;
  }
  .crop-marks { position: absolute; inset: 0; width: 1200px; height: 922px; pointer-events: none; }

  .brochure {
    position: absolute; left: 40px; top: 36px; width: 1122px; height: 844px;
    background: linear-gradient(135deg, var(--navy) 0%, var(--blue) 45%, var(--blue-mid) 75%, var(--blue-light) 100%);
    overflow: hidden;
  }
  .sweep { position: absolute; inset: 0; width: 100%; height: 100%; }

  .panel { position: absolute; top: 0; height: 100%; color: var(--text-light); }
  .panel--left { left: 0; width: 397px; }
  .panel--middle { left: 397px; width: 328px; }
  .panel--right { left: 725px; width: 397px; }

  .heading {
    position: absolute; height: 26px; line-height: 26px;
    background: var(--heading-bar); color: var(--text-light);
    font-weight: 700; font-size: 14.5px; text-transform: uppercase; padding-left: 22px;
  }
  .copy {
    position: absolute; font-size: 14px; line-height: 17.5px; color: var(--text-light);
  }
  .copy ul { list-style: none; }
  .copy li::before { content: "•"; margin-right: 6px; }
  .copy li.sub { padding-left: 22px; }

  .photo { position: absolute; }
  .photo--truck-yard { background: linear-gradient(180deg, #c9d3db 0%, #8b949b 55%, #4d4f4f 100%); }
  .photo--pipe { background: linear-gradient(160deg, #6c4b32 0%, #9a6c45 50%, #3f2d22 100%); }
  .photo--vacuum { background: linear-gradient(180deg, #aebdc9 0%, #d8dcdf 50%, #6f7678 100%); }
  .photo--tank-worker { background: linear-gradient(180deg, #2b3a4d 0%, #4f5e6e 55%, #d5dbe0 100%); }
  .photo--tankers { background: linear-gradient(180deg, #8fb5d9 0%, #c7d1d8 55%, #6a6f72 100%); }
  .photo--boom { background: linear-gradient(180deg, #4a6378 0%, #6a8499 50%, #3b5870 100%); }

  .logo-area {
    position: absolute; left: 0; bottom: 0; width: 397px; height: 150px;
    background: linear-gradient(180deg, rgba(233,238,243,0) 0%, var(--logo-fade) 55%, #ffffff 100%);
  }
  .logo {
    position: absolute; left: 0; right: 0; bottom: 34px;
    display: flex; align-items: center; justify-content: center; gap: 10px;
    font-size: 17px; color: var(--navy); font-weight: 400;
  }
  .logo__mark { width: 12px; height: 12px; background: var(--navy); border-radius: 50%; }
</style>
</head>
<body>
  <div class="sheet-label">BROCHURE | TRI-POINT ENVIRONMENTAL, LLC | CONTENT</div>

  <svg class="crop-marks" viewBox="0 0 1200 922" aria-hidden="true">
    <g stroke="var(--crop)" stroke-width="1">
      <line x1="0" y1="52" x2="28" y2="52"/><line x1="56" y1="24" x2="56" y2="0"/>
      <line x1="1172" y1="52" x2="1200" y2="52"/><line x1="1146" y1="24" x2="1146" y2="0"/>
      <line x1="0" y1="864" x2="28" y2="864"/><line x1="56" y1="892" x2="56" y2="922"/>
      <line x1="1172" y1="864" x2="1200" y2="864"/><line x1="1146" y1="892" x2="1146" y2="922"/>
      <line x1="437" y1="0" x2="437" y2="24"/><line x1="765" y1="0" x2="765" y2="24"/>
      <line x1="437" y1="892" x2="437" y2="922"/><line x1="765" y1="892" x2="765" y2="922"/>
    </g>
  </svg>

  <div class="brochure">
    <svg class="sweep" viewBox="0 0 1122 844" preserveAspectRatio="none" aria-hidden="true">
      <path d="M0 560 C 250 430, 520 470, 760 380 S 1050 260, 1122 250 L1122 330 C 1000 340, 860 430, 700 470 S 300 540, 0 640 Z" fill="#7fb2e0" opacity="0.35"/>
    </svg>

    <section class="panel panel--left">
      <h2 class="heading" style="top:6px;width:397px;">Accident / Spill Cleanup</h2>
      <div class="copy" style="left:22px;top:40px;width:360px;">
        <p>Specialized response equipment and trained personel ensure the most professional cleanup possible.</p>
        <ul>
          <li class="sub">Traffic Control</li>
          <li class="sub">Excavation Equipment</li>
          <li class="sub">Roll-off Containers</li>
          <li>Spill Prevention – Countermeasure Control<br><span style="padding-left:14px">Plans</span></li>
          <li>Removal or Closure of Underground</li>
          <li>Storage Tanks</li>
        </ul>
      </div>
      <div class="photo photo--truck-yard" role="img" aria-label="Vacuum truck parked at a job site" style="left:0;top:302px;width:397px;height:232px;"></div>
      <div class="copy" style="left:22px;top:548px;width:360px;">
        <p>Licensed personel and all of the necessary equipment, PID meter, LEL meter, confined space gear, etc.</p>
        <ul>
          <li>Soil / Groundwater Testing</li>
          <li>Monitoring Well Pumping</li>
        </ul>
      </div>
      <div class="photo photo--pipe" role="img" aria-label="Worker beside a large excavated pipe" style="left:0;top:632px;width:397px;height:212px;"></div>
    </section>

    <section class="panel panel--middle">
      <h2 class="heading" style="top:6px;width:328px;padding-left:8px;">Vacuum Truck Service</h2>
      <div class="copy" style="left:8px;top:40px;width:312px;">
        <p>Dirt and Stone Removal, Product Offloading, Pit Cleaning and Waste Pick Up.</p>
      </div>
      <div class="photo photo--vacuum" role="img" aria-label="Crew working beside a vacuum truck" style="left:0;top:144px;width:328px;height:136px;"></div>
      <h2 class="heading" style="top:286px;width:328px;padding-left:8px;">Tank Cleaning</h2>
      <div class="copy" style="left:8px;top:320px;width:312px;">
        <p>Fuel, Chemical, Fertilizer, Wastewater, Municipal. With our confined space training and rescue equipment, we are able to complete the project safely and to your standards.</p>
      </div>
      <div class="photo photo--tank-worker" role="img" aria-label="Worker in protective suit inside a tank" style="left:0;top:404px;width:328px;height:112px;"></div>
      <h2 class="heading" style="top:524px;width:328px;padding-left:8px;">Bulk Transportations</h2>
      <div class="copy" style="left:8px;top:558px;width:312px;">
        <p>Our vacuum tankers provide around the clock transportation of wastewater and sludge, local or long distance. We can assist with repairs, or pipeline ruptures.</p>
      </div>
      <div class="photo photo--tankers" role="img" aria-label="Fleet of tanker trucks lined up in a yard" style="left:0;top:628px;width:328px;height:216px;"></div>
    </section>

    <section class="panel panel--right">
      <h2 class="heading" style="top:6px;width:397px;">Marine Service / Harbor Boom</h2>
      <div class="copy" style="left:22px;top:40px;width:360px;">
        <p>Total response includes prevention/cleanup on the water. Whether it's a spill or preventative measures, we are prepared. Even large spills are not an issue. Through strategic relationships with other companies specializing in marine cleanup, we can tackle the most difficult situations.</p>
        <ul style="margin-top:28px;"><li>High Pressure Water Blasting.</li></ul>
      </div>
      <div class="photo photo--boom" role="img" aria-label="Containment boom floating on harbor water" style="left:0;top:326px;width:397px;height:212px;"></div>
      <h2 class="heading" style="top:560px;width:397px;">Liquid Storage</h2>
      <div class="copy" style="left:22px;top:594px;width:360px;">
        <p>We have over 100,000 gallons of liquid storage available.</p>
        <ul>
          <li>Disposal of Liquids/Sludge</li>
          <li>Soil Disposal/Remediation</li>
          <li>HAZ Drum Removal</li>
          <li>NON-HAZ Removal</li>
          <li>Lab Pack Disposal</li>
        </ul>
      </div>
      <div class="logo-area">
        <div class="logo"><span class="logo__mark"></span><span>Tri-Point Environmental, LLC</span></div>
      </div>
    </section>
  </div>
</body>
</html>
```